Pilates Studio webdesign - Homepage design

Need a web design for this new Pilates studio.

1) Need elegant design that has great use of stock photos. See attached plumeframe lightbox. Use these for your designs
http://www.frameplume.com/search/lightbox/58120947

Be creative in how you use images. Could be a collage, or single image if design is strong.

2) Also see attached site map (PDF)

3) Please refer to this website for the "rollover section" on homepage. https://www.bookingacademy-varn.com/
We want similar functionality for "I'm Here Because"

4) See attached logos ZIP file.

5) My client kind of likes this website too:
http://motionhallq.com

Target Market(s)

mostly women

Number of Pages Required

2 page

Font styles to use
Sans Serif

Requirements
Must have
• strong design
• good use of stock image(s)
• logo included
Nice to have
• elegant design
Should not have
• not planning to build a long scrolling page.

```html
<!DOCTYPE html>
<html lang="en">
<head>
<meta charset="utf-8">
<title>Motion Hall – Home</title>
<link href="https://fonts.googleapis.com/css2?family=Anton&family=Fira+Sans:wght@300;400;500&display=swap" rel="stylesheet">
<style>
  :root{
    --navy:#13213a;
    --orange:#f7931e;
    --slate:#557393;
    --bg-soft:#f3f3f3;
    --white:#ffffff;
    --text:#555a60;
    --muted:#8fa3bd;
    --heading:#3d3f43;
  }
  *{box-sizing:border-box;margin:0;padding:0}
  html,body{width:972px;height:1200px;overflow:hidden}
  body{position:relative;font-family:"Fira Sans",sans-serif;background:var(--bg-soft);color:var(--text)}
  .abs{position:absolute}

  /* header */
  .site-header{left:0;top:0;width:972px;height:75px;background:var(--navy)}
  .brand{left:60px;top:16px;display:flex;align-items:center;gap:12px}
  .brand-dot{width:42px;height:42px;border-radius:50%;background:var(--orange)}
  .brand-name{font-size:17px;font-weight:500;letter-spacing:1px;color:var(--slate);line-height:1}
  .appt-btn{left:742px;top:11px;width:170px;height:24px;background:var(--orange);color:var(--white);font-size:12px;display:flex;align-items:center;justify-content:center;gap:7px;border-radius:2px}
  .main-nav{right:60px;top:52px;display:flex;gap:27px;font-size:12px;color:var(--white)}
  .main-nav span{padding-bottom:7px}
  .main-nav .active{border-bottom:3px solid var(--orange)}

  /* hero */
  .hero-photo{left:0;top:75px;width:972px;height:508px;background:linear-gradient(100deg,#5b5b5b 0%,#9a9a9a 35%,#c9c9c9 60%,#7c7c7c 100%)}
  .hero-frame{left:60px;top:240px;width:358px;height:181px;border-left:5px solid var(--orange);border-bottom:5px solid var(--orange)}
  .hero-frame-top{left:60px;top:240px;width:183px;height:5px;background:var(--orange)}
  .hero-title{left:108px;top:280px;font-family:"Anton",sans-serif;font-weight:400;font-size:44px;color:var(--white);line-height:1}
  .hero-sub{left:109px;top:331px;font-size:18px;font-weight:400;color:var(--white);line-height:26px}
  .join-card{left:614px;top:423px;width:298px;height:160px;background:var(--slate);text-align:center;color:var(--white)}
  .join-title{margin-top:20px;font-family:"Anton",sans-serif;font-size:27px;line-height:1}
  .join-title em{font-style:normal;color:var(--orange)}
  .join-note{margin-top:10px;font-size:13px;font-weight:500}
  .join-btn{margin:17px auto 0;width:172px;height:46px;background:var(--orange);font-size:13px;font-weight:500;display:flex;align-items:center;justify-content:center}

  /* reasons */
  .section-heading{left:60px;top:620px;width:852px;display:flex;align-items:center;gap:14px}
  .rule{flex:1;height:6px;border-top:1px solid #d8d8d8;border-bottom:1px solid #d8d8d8}
  .section-heading h2{font-family:"Anton",sans-serif;font-weight:400;font-size:29px;color:var(--heading);line-height:1}
  .section-heading h2 em{font-style:normal;color:var(--orange)}
  .reason{top:688px;width:138px;height:138px;border-radius:50%;border:22px solid var(--slate);display:flex;align-items:center;justify-content:center;text-align:center;font-size:13.5px;font-weight:500;color:#4a4d52;line-height:17px}
  .reason.is-active{border-color:var(--orange)}
  .pointer{left:291px;top:829px;width:0;height:0;border-left:17px solid transparent;border-right:17px solid transparent;border-bottom:17px solid var(--white)}
  .info-panel{left:60px;top:846px;width:852px;height:196px;background:var(--white)}
  .info-copy{left:90px;top:870px;width:535px;font-size:11.6px;font-weight:300;line-height:21px;color:var(--text)}
  .divider{left:640px;top:876px;width:3px;height:136px;background:#d4d4d4}
  .cta{left:666px;top:878px;font-family:"Anton",sans-serif;color:var(--orange);line-height:1}
  .cta .small{font-size:33px;letter-spacing:-.3px;opacity:.9}
  .cta .big{font-size:42px;margin-top:5px}
  .cta .big + .big{display:flex;align-items:center;gap:10px}

  /* footer */
  .site-footer{left:0;top:1087px;width:972px;height:113px;background:var(--navy)}
  .contact{top:1107px;display:flex;gap:10px;font-size:11px;color:var(--muted);line-height:17px}
  .socials{right:60px;top:1108px;display:flex;gap:4px}
  .socials span{width:30px;height:30px;background:var(--slate);display:flex;align-items:center;justify-content:center}
  .footer-bar{left:0;top:1160px;width:972px;height:1px;background:#26344d}
  .copyright{left:0;top:1173px;width:972px;text-align:center;font-size:11px;color:var(--muted)}
</style>
</head>
<body>

<header class="site-header abs">
  <div class="brand abs">
    <div class="brand-dot"></div>
    <div class="brand-name">MOTION HALL</div>
  </div>
  <div class="appt-btn abs">
    <svg width="12" height="11" viewBox="0 0 12 11"><rect x="1" y="2" width="10" height="8" fill="none" stroke="#fff" stroke-width="1.2"/><line x1="1" y1="4.5" x2="11" y2="4.5" stroke="#fff"/><line x1="4" y1="0.5" x2="4" y2="3" stroke="#fff"/><line x1="8" y1="0.5" x2="8" y2="3" stroke="#fff"/></svg>
    MAKE AN APPOINTMENT
  </div>
  <nav class="main-nav abs">
    <span class="active">ABOUT MARLOWE</span>
    <span>WHAT IS MOTION</span>
    <span>HALL</span>
    <span>SCHEDULING</span>
    <span>SESSIONS</span>
    <span>REFERRALS</span>
  </nav>
</header>

<div class="hero-photo abs" role="img" aria-label="Black and white photo of a woman hanging from a Pilates trapeze table in a bright studio"></div>
<div class="hero-frame abs"></div>
<div class="hero-frame-top abs"></div>
<h1 class="hero-title abs">MOTION HALL</h1>
<p class="hero-sub abs">is about a movement in the now to<br>change your life for the bee better</p>

<div class="join-card abs">
  <div class="join-title">JOIN NOW FOR <em>JUST $99</em></div>
  <div class="join-note">Include FREE BodyScan Consultation</div>
  <div class="join-btn">JOIN NOW</div>
</div>

<div class="section-heading abs">
  <div class="rule"></div>
  <h2>I'M HERE <em>BECAUSE</em></h2>
  <div class="rule"></div>
</div>

<div class="reason abs" style="left:60px">Pilates</div>
<div class="reason is-active abs" style="left:238px">Back &amp; Joint<br>Pain</div>
<div class="reason abs" style="left:417px">Stretching</div>
<div class="reason abs" style="left:595px">Mobility &amp;<br>Stability</div>
<div class="reason abs" style="left:774px">Strengthen<br>Body</div>

<div class="pointer abs"></div>
<div class="info-panel abs"></div>
<p class="info-copy abs">Lorem Ipsum is simply dummy text of the printing and typesetting industry. Lorem Ipsum has been the industry's standard dummy text ever since the 1500s, when an unknown printer took a galley of type and scrambled it to make a type specimen book. It has survived not only five centuries, but also the leap into electronic typesetting, remaining essentially unchanged. It was popularised in the 1960s with the release of Letraset sheets containing Lorem Ipsum passages, and more recently with desktop publishing software like Aldus PageMaker including versions of Lorem Ipsum.</p>
<div class="divider abs"></div>
<div class="cta abs">
  <div class="small">CLICK TO LEARN</div>
  <div class="big">HOW WE CAN</div>
  <div class="big">HELP YOU
    <svg width="22" height="22" viewBox="0 0 22 22" fill="none" stroke="var(--orange)" stroke-width="2"><circle cx="11" cy="11" r="9.5"/><path d="M9 6.5 L13.5 11 L9 15.5"/></svg>
  </div>
</div>

<footer class="site-footer abs"></footer>
<div class="contact abs" style="left:60px">
  <svg width="16" height="26" viewBox="0 0 16 26" fill="none" stroke="var(--muted)" stroke-width="1.3"><path d="M8 24 C3 16 1 12 1 8 A7 7 0 0 1 15 8 C15 12 13 16 8 24Z"/><circle cx="8" cy="8" r="2.5"/></svg>
  <div>228, Lorem dolor Ipsum,<br>Street Area, City - 185484</div>
</div>
<div class="contact abs" style="left:241px">
  <svg width="20" height="22" viewBox="0 0 20 22" fill="none" stroke="var(--muted)" stroke-width="1.3"><path d="M4 2 L8 6 L6 9 C7 12 9 14 12 16 L15 14 L19 18 L16 21 C9 20 2 13 1 5Z"/><path d="M12 3 A6 6 0 0 1 18 9"/></svg>
  <div>Call Us :<br>1800 555 0142</div>
</div>
<div class="contact abs" style="left:374px">
  <svg width="28" height="20" viewBox="0 0 28 20" fill="none" stroke="var(--muted)" stroke-width="1.3"><rect x="1" y="1" width="26" height="18"/><path d="M1 1 L14 12 L27 1"/><path d="M1 19 L11 10 M27 19 L17 10"/></svg>
  <div>Email Us :<br>info@motionhall.com</div>
</div>
<div class="socials abs">
  <span></span><span></span><span></span><span></span>
  <span><svg width="18" height="18" viewBox="0 0 18 18" fill="var(--navy)" stroke="var(--navy)" stroke-width="2"><circle cx="14" cy="4" r="2.5"/><circle cx="4" cy="9" r="2.5"/><circle cx="14" cy="14" r="2.5"/><path d="M14 4 L4 9 L14 14" fill="none"/></svg></span>
</div>
<div class="footer-bar abs"></div>
<div class="copyright abs">©Copyright 2016 Motion Hall All Rights Reserved. Privacny Policy | Sitemap</div>

</body>
</html>
```